Stationary design and implementation for Swedish IT company

Hi,

I'm looking for a design and statiionary for my company (www.lumaverk.example).

Lumaverk is an innovative company with four core values:
- Entrepreneurial; we take risks and the responsibility to create value
- Awarding; we work with fun and have added value to our relationships
- Innovation; we're creative and introduce new solutions
- Respect; we work with respect for our environment based on values instead of red tape

The required stationary should include:
- Powerpoint template
- Word templates
- Business card design
- e-mail signature

Please visit our site for more details.
Updates

Hi - please read (PRIORITY!),

You have been involved in one my projects. 

As it seems there is something seriously wrong with the participation payments at ArtFolkHub. 

I have send invites with participation payments to reward designers for there work. It has been reported that these invitations resulted in expired messages, and payments have NOT been made. The money is withdrawn from my account and NOT paid to designers. This is a real shame when people do not get rewarded for the work done and the money is gone.

When you got an invitation with participation payment could you please let me know if the payment has actually been made? You can contact me at hmelsted@lumaverk.example.

I'm trying to get this clarified with ArtFolkHub.

Grt, Joost

Target Market(s)

Our market is IT and professional service in Sweden and other Nordics countries (Danmark, Norway, Finland).

Industry/Entity Type

Environment

Requirements
Must have
• Project delivery should include:
- Powerpoint template with title and content pages
- Standard letter (Word template)
- Standard invoice (Word template)
- Business card
- e-mail signature
Should not have
• Please await a logo to be attached (almost done).

```html
<!DOCTYPE html>
<html lang="en">
<head>
<meta charset="utf-8">
<title>Lumaverk business cards</title>
<link rel="stylesheet" href="https://fonts.googleapis.com/css2?family=Source+Sans+3:wght@400;600&display=swap">
<style>
  :root {
    --backdrop: #1c2a5a;
    --card: #ffffff;
    --navy: #1f2b63;
    --blue: #2f5bb0;
    --ink-grey: #555a60;
    --soft-grey: #e4e4e6;
    --text-dark: #2a2a2a;
    --shadow: rgba(0, 0, 0, 0.35);
  }
  * { box-sizing: border-box; margin: 0; padding: 0; }
  html, body { width: 1200px; height: 900px; overflow: hidden; }
  body {
    background: var(--backdrop);
    font-family: "Source Sans 3", sans-serif;
    position: relative;
  }
  .card {
    position: absolute;
    width: 512px;
    height: 294px;
    background: var(--card);
    box-shadow: 4px 6px 10px var(--shadow);
    overflow: hidden;
  }
  .card--front { left: 68px; top: 64px; }
  .card--logo { left: 620px; top: 280px; }
  .card--back { left: 66px; top: 482px; }

  .brand { position: absolute; }
  .brand__dot {
    position: absolute;
    width: 62px; height: 62px;
    border-radius: 50%;
    background: var(--blue);
  }
  .brand__name {
    position: absolute;
    font-weight: 600;
    font-size: 82px;
    line-height: 1;
    color: var(--navy);
    letter-spacing: -1px;
    white-space: nowrap;
  }
  .card--front .brand__dot { left: 30px; top: 74px; }
  .card--front .brand__name { left: 126px; top: 60px; }
  .card--logo .brand__dot { left: 30px; top: 116px; }
  .card--logo .brand__name { left: 126px; top: 102px; }

  .band { position: absolute; }
  .band--blue { left: 276px; top: 240px; width: 236px; height: 16px; background: var(--blue); }
  .band--navy { left: 146px; top: 256px; width: 366px; height: 16px; background: var(--navy); }

  .back__decor {
    position: absolute;
    left: 10px; top: 10px;
    width: 220px; height: 160px;
    border-radius: 50%;
    background: radial-gradient(circle, rgba(228,228,230,0.9) 0%, rgba(228,228,230,0) 70%);
  }
  .person { position: absolute; right: 16px; text-align: right; }
  .person__name {
    position: absolute; right: 0; top: 20px;
    font-weight: 600; font-size: 46px; line-height: 1;
    color: var(--ink-grey); white-space: nowrap;
  }
  .person__title {
    position: absolute; right: 0; top: 74px;
    font-size: 27px; line-height: 1; font-weight: 400;
    color: var(--ink-grey); white-space: nowrap;
  }
  .contact {
    position: absolute;
    display: flex; align-items: center;
    font-size: 16px; color: var(--text-dark);
    white-space: nowrap;
  }
  .contact__badge {
    width: 44px; height: 26px;
    border-radius: 50%;
    background: var(--navy);
    color: #fff;
    font-weight: 600; font-size: 17px;
    display: flex; align-items: center; justify-content: center;
    margin-right: 8px;
  }
  .contact--email { left: 14px; top: 151px; }
  .contact--web { left: 14px; top: 185px; }
  .contact--social { left: 14px; top: 219px; }
  .contact--mobile { left: 314px; top: 185px; }
  .contact--phone { left: 314px; top: 219px; }
  .address {
    position: absolute;
    left: 62px; top: 258px;
    font-size: 15.5px; color: var(--text-dark);
    white-space: nowrap;
  }
</style>
</head>
<body>

  <section class="card card--front" aria-label="Business card front">
    <div class="brand">
      <span class="brand__dot" aria-hidden="true"></span>
      <span class="brand__name">Lumaverk</span>
    </div>
    <span class="band band--blue" aria-hidden="true"></span>
    <span class="band band--navy" aria-hidden="true"></span>
  </section>

  <section class="card card--logo" aria-label="Business card logo side">
    <div class="brand">
      <span class="brand__dot" aria-hidden="true"></span>
      <span class="brand__name">Lumaverk</span>
    </div>
  </section>

  <section class="card card--back" aria-label="Business card contact side">
    <span class="back__decor" aria-hidden="true"></span>
    <div class="person">
      <h1 class="person__name">Joost Melsted</h1>
      <p class="person__title">Job Title</p>
    </div>
    <p class="contact contact--email"><span class="contact__badge">E</span>hmelsted@lumaverk.example</p>
    <p class="contact contact--web"><span class="contact__badge">W</span>www.lumaverk.example</p>
    <p class="contact contact--social"><span class="contact__badge" aria-hidden="true"></span>social.example/lumaverk</p>
    <p class="contact contact--mobile"><span class="contact__badge">M</span>++ (0) 555 01 2345</p>
    <p class="contact contact--phone"><span class="contact__badge">T</span>++ (0) 555 01 2345</p>
    <p class="address">1234 address line 1 - address line 2 - address line 3 - area code</p>
  </section>

</body>
</html>
```